Wordpress Identity for Innovation Firm

Copper Lantern Partners is an innovation and investment firm based in Los Angeles.

We are seeking a designer that can help create our company identity and Wordpress site.

The attached Design Brief provides more details.

Designers Responsibility:

1) Company Identity

The designer will create the company identity.
Attached is a file that contains a type font that I like a lot.
No logo design is required.

The Copper Lantern Partners type font should become the company identity.
The attached document provides an overview of company type font identities that we like.

2) Wordpress Theme & Design

The designer will select existing Wordpress Themes that meet our design desires, and present them as part of the design proposal.

We will make our selection based on the selected Wordpress Theme(s), which the designer will creatively adapt with the new company identity.

Target Market(s)

We anticipate the website being mostly accessed by the US, Canada and European countries.

Our target audience includes the following:

• Corporations, companies, startups, non-profits
• Banks, venture capital, private equity, investors
• Incubators, accelerators, innovation clusters, research labs, universities
• Ad agencies, marketing agencies, digital agencies, media, press

Industry/Entity Type

Investment

Number of Pages Required

1 page

Font styles to use
Sans Serif
Other font styles liked:
• See attached design brief materials. The Font will represent the brand identity!

Requirements
Must have
• The ability to scroll through information top to bottom is important to us.
• This is in line with today's Wordpress themes.
• The website must be able to function across devices (desktop, tablet, phone).
• The top 5 web browsers and platforms (Mac/PC/Android/iOS)
• Contact us link or information field
Nice to have
• It would be nice to have a moving image in the background, such as:
• https://drifttrial.sitehatch.com
• The Wordpress theme of the moving image or video should be relevant to our overall Technology Innovation theme.
• Key words:
• Technology Innovation
• Digital
• Business
• Transportation
• Advanced Vehicles (auto, boat, airplane, rail, space)
• Space
• Venture Capital
• Investing
Should not have
• eCommerce

```html
<!DOCTYPE html>
<html lang="en">
<head>
<meta charset="utf-8">
<title>Copper Lantern Partners</title>
<link rel="stylesheet" href="https://fonts.googleapis.com/css2?family=Open+Sans:wght@400;600;700;800&display=swap">
<style>
:root{
  --white:#ffffff;
  --ink:#222222;
  --muted:#777777;
  --rule:#dddddd;
  --dark:#2b2b2b;
  --darker:#1c1c1c;
  --heading:#555555;
}
*{box-sizing:border-box;margin:0;padding:0}
html,body{width:716px;height:1200px;overflow:hidden}
body{position:relative;font-family:"Open Sans",Arial,sans-serif;color:var(--ink);background:var(--white)}
.block{position:absolute;left:0;width:716px}

/* header */
.site-header{top:0;height:67px;background:var(--white);border-bottom:1px solid var(--rule)}
.brand{position:absolute;left:14px;top:22px;font-weight:700;font-size:15px;color:var(--ink)}
.utility{position:absolute;right:16px;top:8px;font-size:8px;color:var(--muted);display:flex;gap:12px;align-items:center}
.utility span{display:flex;align-items:center;gap:4px}
.main-nav{position:absolute;left:312px;top:40px;display:flex;gap:14px;font-size:8px;font-weight:600;color:var(--ink)}
.search{position:absolute;right:16px;top:36px;width:118px;height:16px;border:1px solid var(--rule);font-size:7px;color:#aaa;padding:3px 6px;display:flex;justify-content:space-between;align-items:center}

/* hero */
.hero{top:67px;height:370px;background:linear-gradient(180deg,#b9b9b9 0%,#8f8f8f 35%,#5a5a5a 62%,#3a3a3a 100%)}
.hero-title{position:absolute;top:118px;width:100%;text-align:center;color:var(--white);font-weight:800;font-size:29px;letter-spacing:1px}
.hero-text{position:absolute;top:172px;left:160px;width:396px;text-align:center;color:var(--white);font-size:10px;line-height:14px}
.btn{display:inline-block;border:1px solid var(--white);color:var(--white);font-size:8px;padding:6px 16px;background:rgba(0,0,0,.25)}
.hero .btn{position:absolute;top:266px;left:318px}
.arrow{position:absolute;top:175px}

/* about */
.about{top:437px;height:238px}
.photo{position:absolute}
.about-left{left:0;top:0;width:358px;height:238px;background:linear-gradient(135deg,#6a6a6a,#2e2e2e 60%,#1f1f1f)}
.about-right{left:358px;top:0;width:358px;height:238px;background:radial-gradient(circle at 78% 30%,#d8d8d8 0,#8c8c8c 18%,#3c3c3c 48%,#252525 100%)}
.about-tri{position:absolute;left:0;top:0}
.about-heading{position:absolute;top:30px;width:100%;text-align:center;font-size:20px;font-weight:400;color:var(--heading)}
.about-text{position:absolute;top:66px;left:298px;width:120px;text-align:center;font-size:6.5px;line-height:10px;color:var(--muted)}
.about-more{position:absolute;top:150px;width:100%;text-align:center;font-size:7px;color:var(--ink);font-weight:600}
.about-claim{position:absolute;top:136px;color:var(--white);font-size:15px;line-height:20px}
.claim-left{left:16px;width:250px}
.claim-right{left:444px;width:262px}

/* partnerships */
.partners{top:675px;height:208px}
.partners-left{left:0;top:0;width:239px;height:208px;background:linear-gradient(160deg,#f2f2f2,#bdbdbd 60%,#8d8d8d)}
.partners-right{left:477px;top:0;width:239px;height:208px;background:linear-gradient(200deg,#ffffff,#d6d6d6 55%,#9a9a9a)}
.partners-box{position:absolute;left:239px;top:0;width:238px;height:208px;background:var(--darker);color:var(--white);text-align:center}
.partners-box h2{margin-top:34px;font-size:17px;font-weight:600}
.partners-box p{margin:12px auto 0;width:196px;font-size:6.5px;line-height:10px;color:#cccccc}
.partners-box .btn{margin-top:16px}

/* contact */
.contact{top:883px;height:239px}
.feed{left:0;top:0;width:358px;height:239px;background:var(--dark)}
.map{left:358px;top:0;width:358px;height:239px;background:linear-gradient(135deg,#e7e3da,#cfd3cc 45%,#b8c4c8)}
.feed-text{position:absolute;left:16px;top:100px;width:150px;font-size:6.5px;line-height:10px;color:#c8c8c8}
.feed-text .handle{display:block;margin-top:8px}
.contact-tri{position:absolute;left:0;top:0}
.contact-heading{position:absolute;top:90px;width:100%;text-align:center;font-size:20px;font-weight:400;color:var(--heading)}
.contact-list{position:absolute;top:128px;left:318px;list-style:none;font-size:7px;line-height:12px;color:var(--muted)}
.contact-list li{display:flex;gap:6px;align-items:flex-start;margin-bottom:6px}

/* footer */
.site-footer{top:1122px;height:78px;background:#111111;color:#bbbbbb;text-align:center}
.social{display:flex;justify-content:center;gap:10px;padding-top:16px}
.social span{width:18px;height:18px;border:1px solid #bbbbbb;border-radius:50%}
.copyright{margin-top:12px;font-size:7px}
</style>
</head>
<body>

<header class="block site-header">
  <div class="brand">Copper Lantern Partners</div>
  <div class="utility">
    <span><svg width="8" height="6" viewBox="0 0 8 6"><rect x=".5" y=".5" width="7" height="5" fill="none" stroke="#777"/><path d="M.5 .5 4 3.5 7.5 .5" fill="none" stroke="#777"/></svg>hello@copperlantern.example</span>
    <span><svg width="7" height="7" viewBox="0 0 7 7"><circle cx="3.5" cy="2" r="1.6" fill="#777"/><path d="M0 7a3.5 3 0 0 1 7 0z" fill="#777"/></svg>Log in | Register</span>
  </div>
  <nav class="main-nav"><span>HOME</span><span>ABOUT US</span><span>SERVICES</span><span>CONTACT US</span></nav>
  <div class="search">Search <svg width="7" height="7" viewBox="0 0 7 7"><circle cx="3" cy="3" r="2.2" fill="none" stroke="#999"/><path d="M4.6 4.6 6.6 6.6" stroke="#999"/></svg></div>
</header>

<section class="block hero" role="img" aria-label="Black and white city skyline with mountains behind">
  <h1 class="hero-title">COPPER LANTERN PARTNERS</h1>
  <p class="hero-text">Copper Lantern Partners' mission is to create sustainable competitive advantage through market innovation and long-term growth partnerships, and the ability to provide dedicated partnership models.</p>
  <span class="btn">Read More</span>
  <svg class="arrow" style="left:12px" width="10" height="16" viewBox="0 0 10 16"><path d="M8 1 2 8l6 7" fill="none" stroke="#fff" stroke-width="2.5"/></svg>
  <svg class="arrow" style="right:12px" width="10" height="16" viewBox="0 0 10 16"><path d="M2 1l6 7-6 7" fill="none" stroke="#fff" stroke-width="2.5"/></svg>
</section>

<section class="block about">
  <div class="photo about-left" role="img" aria-label="Hands fitting puzzle pieces together on a dark background"></div>
  <div class="photo about-right" role="img" aria-label="Glowing light bulb on a dark background"></div>
  <svg class="about-tri" width="716" height="238" viewBox="0 0 716 238"><polygon points="191,0 525,0 358,238" fill="#fff"/></svg>
  <h2 class="about-heading">About Us</h2>
  <p class="about-text">Copper Lantern is a young and dynamic digital technology and investment firm, which will be recognized by its ability to transform sustainable innovations by co-creating innovative businesses.</p>
  <div class="about-more">Read More &gt;&gt;</div>
  <p class="about-claim claim-left">Support European small and midsized companies expand into North America.</p>
  <p class="about-claim claim-right">Build digital companies around innovative concepts in partnership with corporations.</p>
</section>

<section class="block partners">
  <div class="photo partners-left" role="img" aria-label="Hand pulling a block from a wooden block tower"></div>
  <div class="photo partners-right" role="img" aria-label="Small figures carrying large puzzle pieces on a light background"></div>
  <div class="partners-box">
    <h2>We build Partnerships</h2>
    <p>Copper Lantern Partners introduces a new way of thinking and doing in order to create growth in emerging competitive environments. Most large companies are designed to maximize efficiency, minimize variances and avoid experimentation.</p>
    <span class="btn">Read More</span>
  </div>
</section>

<section class="block contact">
  <div class="photo feed">
    <svg style="position:absolute;left:16px;top:56px" width="22" height="22"><circle cx="11" cy="11" r="10" fill="#fff"/></svg>
    <p class="feed-text">Our new field notes "Lanterns in the Fog" on how great ideas come from simple observation and clear thinking. #innovation #ventures<span class="handle">- @CopperLanternPtnrs</span></p>
  </div>
  <div class="photo map" role="img" aria-label="Street map of Los Angeles"></div>
  <svg class="contact-tri" width="716" height="239" viewBox="0 0 716 239"><polygon points="358,0 537,239 167,239" fill="#fff"/></svg>
  <h2 class="contact-heading">Contact Us</h2>
  <ul class="contact-list">
    <li><svg width="7" height="10" viewBox="0 0 7 10"><path d="M3.5 10C1 6 0 4.6 0 3.5a3.5 3.5 0 0 1 7 0C7 4.6 6 6 3.5 10z" fill="#888"/><circle cx="3.5" cy="3.5" r="1.2" fill="#fff"/></svg><span>Copper Lantern Partners<br>Los Angeles</span></li>
    <li><svg width="8" height="8" viewBox="0 0 8 8"><path d="M1 .5h2l.8 2-1.2.8a5 5 0 0 0 2.1 2.1l.8-1.2 2 .8v2a1 1 0 0 1-1 1A6.5 6.5 0 0 1 0 1.5a1 1 0 0 1 1-1z" fill="#888"/></svg><span>1 (555) 014-2290</span></li>
    <li><svg width="8" height="6" viewBox="0 0 8 6"><rect x=".5" y=".5" width="7" height="5" fill="none" stroke="#888"/><path d="M.5 .5 4 3.5 7.5 .5" fill="none" stroke="#888"/></svg><span>hello@copperlantern.example</span></li>
  </ul>
</section>

<footer class="block site-footer">
  <div class="social"><span></span><span></span><span></span><span></span></div>
  <p class="copyright">Copyright © 2015 Copper Lantern Partners . All rights are reserved.</p>
</footer>

</body>
</html>
```